Brochure design for 3D ultrasound company

I am looking for a clean and modern and edgy brochure for my ultrasound company. We are a fairly new company specialize in 3D/4D ultrasounds.Our brochures will be placed in OB-GYN offices in high end areas around Los Angeles, so we need something that will stand out and capture a modern woman's attention. Our logo is currently in the process of being designed, so I don't have a picture to provide quite yet, however it will be our company name"Kite + Lantern" written in a special font that looks like neon lights. I will attach a few images of what our logo will be like, and some initial content that can help provide the layout we would like for the brochure. please feel free to also take a look at our website. www.kitelanternscan.example.

Target Market(s)

Upscale trendy women.

Colors
eea4c8
33a6d7
fee18a

Requirements
Should not have
• too many colors.

```html
<!DOCTYPE html>
<html lang="en">
<head>
<meta charset="utf-8">
<title>Kite + Lantern — Tri-fold Brochure</title>
<link rel="stylesheet" href="https://fonts.googleapis.com/css2?family=Jost:wght@300;400;500&family=Montserrat:wght@800;900&display=swap">
<style>
  :root {
    --blue: #33a6d7;
    --blue-deep: #2a6fc0;
    --pink: #eea4c8;
    --pink-text: #e98fb3;
    --pink-strong: #f08cb4;
    --black: #0d0d0d;
    --white: #ffffff;
    --ink: #3a3a3a;
    --page: #ececec;
  }
  * { box-sizing: border-box; margin: 0; padding: 0; }
  html, body { width: 1059px; height: 1200px; overflow: hidden; }
  body { background: var(--page); font-family: "Jost", sans-serif; position: relative; }

  .spread { position: absolute; left: 24px; width: 1011px; height: 570px; overflow: hidden; box-shadow: 0 4px 14px rgba(0,0,0,.18); }
  .spread--outside { top: 20px; }
  .spread--inside { top: 610px; background: var(--pink); }
  .panel { position: absolute; top: 0; width: 337px; height: 570px; overflow: hidden; }
  .panel--1 { left: 0; } .panel--2 { left: 337px; } .panel--3 { left: 674px; }

  .photo { position: absolute; }

  /* wordmark */
  .wordmark { display: flex; align-items: center; gap: 8px; color: var(--white); font-family: "Jost", sans-serif; font-weight: 300; font-size: 34px; letter-spacing: 1px; white-space: nowrap; }
  .wordmark__dot { width: 10px; height: 10px; border-radius: 50%; background: var(--pink); flex: none; }

  /* outside: intro panel */
  .intro { background: var(--blue); }
  .intro__headline { position: absolute; top: 36px; right: 22px; width: 300px; text-align: right; font-family: "Montserrat", sans-serif; font-weight: 800; font-size: 31px; line-height: 1.05; color: var(--pink); text-transform: uppercase; text-shadow: 1px 2px 2px rgba(0,0,0,.35); }
  .intro__body { position: absolute; left: 28px; width: 285px; color: var(--white); font-weight: 300; font-size: 14px; line-height: 1.4; }
  .intro__body--about { top: 200px; }
  .intro__body--mission { top: 312px; left: 38px; }
  .intro__photo { left: 34px; top: 402px; width: 270px; height: 150px; background: linear-gradient(90deg, #f0a9b8 0%, #f6d8cc 50%, #bcd9c4 100%); }

  /* outside: contact panel */
  .contact { background: var(--blue); }
  .contact__photo { left: 0; top: 0; width: 337px; height: 250px; background: linear-gradient(180deg, #f4f4f4, #e3dcd6 70%, #9fb3c8); }
  .contact__wordmark { position: absolute; top: 286px; left: 0; width: 337px; justify-content: center; }
  .contact__phone { position: absolute; top: 352px; width: 337px; text-align: center; color: var(--white); font-weight: 300; font-size: 32px; }
  .contact__list { position: absolute; top: 410px; width: 337px; list-style: none; text-align: center; color: var(--white); font-weight: 300; font-size: 14px; line-height: 2.25; }

  /* outside: cover panel */
  .cover { background: var(--black); }
  .cover__wordmark { position: absolute; top: 42px; left: 0; width: 337px; justify-content: center; }
  .cover__tagline { position: absolute; top: 104px; width: 337px; text-align: center; color: var(--white); font-weight: 500; font-size: 15px; }
  .cover__photo { left: 0; top: 140px; width: 337px; height: 430px; background: linear-gradient(180deg, #3b4c5c 0%, #7fbfe0 25%, #9fd0ea 60%, #6fb2d8 100%); }
  .cover__silhouette { position: absolute; left: 0; top: 0; }
  .cover__claim { position: absolute; top: 408px; width: 337px; text-align: center; color: var(--white); font-weight: 500; font-size: 19px; line-height: 1.15; text-transform: uppercase; text-shadow: 0 1px 3px rgba(0,0,0,.4); }
  .cover__cta { position: absolute; top: 468px; width: 337px; text-align: center; color: var(--pink-strong); font-weight: 300; font-size: 34px; line-height: 1; text-transform: uppercase; }
  .cover__phone { position: absolute; top: 508px; width: 337px; text-align: center; color: var(--pink-strong); font-weight: 500; font-size: 32px; letter-spacing: 1px; }

  /* inside */
  .doll-strip { position: absolute; left: 0; top: 0; width: 1011px; height: 46px; background: linear-gradient(90deg, #f6c9cc, #f3bcc3 50%, #f6c9cc); border-bottom: 4px solid #bfe3f0; }
  .inside__header { position: absolute; left: 0; top: 50px; width: 674px; height: 170px; background: var(--black); }
  .inside__wordmark { position: absolute; top: 104px; left: 24px; }
  .inside__couple { left: 337px; top: 50px; width: 337px; height: 190px; background: linear-gradient(90deg, #b9876a, #7c8fa8 55%, #d9c2b6); }
  .inside__backdrop { left: 0; top: 220px; width: 674px; height: 350px; background: linear-gradient(90deg, #eea4c8, #f0b6d2 35%, #d9a3c7 60%, #eea4c8); }

  .packages__popular { position: absolute; left: 22px; top: 228px; width: 140px; font-family: "Montserrat", sans-serif; font-weight: 900; font-size: 16px; line-height: 1; color: var(--blue); text-transform: uppercase; }
  .packages__note { position: absolute; left: 168px; top: 256px; width: 500px; text-align: center; color: var(--white); font-weight: 500; font-size: 10.5px; line-height: 1.25; text-transform: uppercase; text-shadow: 0 1px 1px rgba(0,0,0,.35); }
  .package { position: absolute; top: 292px; width: 168px; height: 260px; padding: 0 10px; text-align: center; }
  .package + .package { border-left: 2px solid var(--blue-deep); }
  .package--reveal { left: 0; top: 284px; height: 268px; }
  .package--mama { left: 168px; }
  .package--vib { left: 337px; }
  .package--peek { left: 505px; }
  .package__name { font-family: "Montserrat", sans-serif; font-weight: 800; font-size: 15px; line-height: 1; color: var(--white); text-transform: uppercase; text-shadow: 1px 1px 0 #222; }
  .package__sub { font-size: 10.5px; font-style: italic; color: var(--white); font-weight: 300; }
  .package__items { list-style: none; margin-top: 6px; color: var(--ink); font-size: 13px; line-height: 1.08; }
  .package__items li { margin-bottom: 6px; }
  .package__items li::before { content: "• "; }
  .package__price { position: absolute; left: 0; bottom: 0; width: 100%; text-align: center; color: var(--white); font-weight: 300; font-size: 22px; }

  .glossary { background: var(--white); top: 50px; height: 520px; }
  .glossary__title { position: absolute; top: 14px; left: 18px; font-family: "Montserrat", sans-serif; font-weight: 900; font-size: 23px; color: var(--black); text-transform: uppercase; }
  .glossary__list { position: absolute; top: 54px; left: 22px; width: 296px; font-size: 13.5px; line-height: 1.15; font-weight: 300; }
  .glossary__item { margin-bottom: 12px; }
  .glossary__item--blue { color: var(--blue-deep); }
  .glossary__item--pink { color: var(--pink-text); }
  .glossary__term { font-family: "Montserrat", sans-serif; font-weight: 900; }
  .glossary__photo { left: 10px; top: 374px; width: 317px; height: 140px; background: linear-gradient(180deg, #f2efee, #e6dcd6 55%, #3a3a3a); }
</style>
</head>
<body>

<section class="spread spread--outside">
  <article class="panel panel--1 intro">
    <h1 class="intro__headline">Ready for your baby’s first photo shoot?</h1>
    <p class="intro__body intro__body--about">KITE + LANTERN is a mobile 3D ultrasound company servicing Los Angeles, and surrounding areas. We take great pride in being one of LA’s first mobile ultrasound companies and for being an all female business!</p>
    <p class="intro__body intro__body--mission">Our mission is to provide an unforgettable experience for expectant mothers in the comfort of their home!</p>
    <div class="photo intro__photo" role="img" aria-label="Photo of two expectant mothers in crop tops and jeans showing their bellies"></div>
  </article>

  <article class="panel panel--2 contact">
    <div class="photo contact__photo" role="img" aria-label="Photo of an expectant mother in a white tee and jeans posing on a white backdrop"></div>
    <div class="wordmark contact__wordmark"><span>Kite + Lantern</span><span class="wordmark__dot"></span></div>
    <p class="contact__phone">(310) 555-0142</p>
    <ul class="contact__list">
      <li>www.kitelanternscan.example</li>
      <li>info@kitelanternscan.example</li>
      <li>Instagram: kite_lantern</li>
      <li>Facebook: @kitelanternscan</li>
    </ul>
  </article>

  <article class="panel panel--3 cover">
    <div class="photo cover__photo" role="img" aria-label="Blue-toned photo of an expectant mother holding a strip of ultrasound prints"></div>
    <svg class="cover__silhouette" width="337" height="570" viewBox="0 0 337 570" aria-hidden="true">
      <path d="M0 0 H34 C20 40 46 70 26 110 C10 140 40 160 30 200 L0 200 Z" fill="#33a6d7"/>
    </svg>
    <div class="wordmark cover__wordmark"><span>Kite + Lantern</span><span class="wordmark__dot"></span></div>
    <p class="cover__tagline">A mobile 3D/4D ultrasound service</p>
    <p class="cover__claim">Ultrasound in the<br>comfort of your home</p>
    <p class="cover__cta">Call today!</p>
    <p class="cover__phone">310-555-0142</p>
  </article>
</section>

<section class="spread spread--inside">
  <div class="doll-strip" role="img" aria-label="Photo band of a row of baby dolls on a pink background"></div>
  <div class="inside__header"></div>
  <div class="photo inside__couple" role="img" aria-label="Photo of a couple holding boy and girl notes over a pregnant belly in denim overalls"></div>
  <div class="photo inside__backdrop" role="img" aria-label="Faint pink-toned photo of an expectant mother"></div>
  <div class="wordmark inside__wordmark"><span>Kite + Lantern</span><span class="wordmark__dot"></span></div>

  <p class="packages__popular">Our most popular package!</p>
  <p class="packages__note">Available for private, in-home screenings, gender reveals,<br>baby showers, or any other special occasions!</p>

  <div class="package package--reveal">
    <h2 class="package__name">The Big<br>Reveal:</h2>
    <ul class="package__items">
      <li>25-minute 3D/4D/HD live session</li>
      <li>5 black &amp; white pictures</li>
      <li>5 color pictures</li>
      <li>Email or USB flash drive with all images</li>
      <li>Record &amp; hear heartbeat</li>
      <li>Confirm gender</li>
    </ul>
    <p class="package__price">$225.00</p>
  </div>
  <div class="package package--mama">
    <h2 class="package__name">Hello<br>Mama:</h2>
    <ul class="package__items">
      <li>15-minute 3D/4D/HD live session</li>
      <li>3 black &amp; white pictures</li>
      <li>2 color pictures</li>
      <li>Listen to baby’s heartbeat</li>
      <li>Confirm gender</li>
    </ul>
    <p class="package__price">$165.00</p>
  </div>
  <div class="package package--vib">
    <h2 class="package__name">V.I.B.</h2>
    <p class="package__sub">(very important baby)</p>
    <ul class="package__items">
      <li>30-minute 3D/4D/HD live session on our projector</li>
      <li>10 color pictures</li>
      <li>Email or USB with all images</li>
      <li>Listen to baby’s heartbeat</li>
      <li>Confirm gender</li>
    </ul>
    <p class="package__price">$325.00</p>
  </div>
  <div class="package package--peek">
    <h2 class="package__name">Peek-a-boo:</h2>
    <ul class="package__items">
      <li>15-minute 2D session</li>
      <li>3 black &amp; white pictures</li>
      <li>Listen to baby’s heartbeat</li>
      <li>Confirm gender</li>
    </ul>
    <p class="package__price">$125.00</p>
  </div>

  <article class="panel panel--3 glossary">
    <h2 class="glossary__title">What’s what …</h2>
    <div class="glossary__list">
      <p class="glossary__item glossary__item--blue"><span class="glossary__term">2D</span> is the traditional black-and-white photo - You know, the one that you want to get emotional about, but you don’t know what you’re looking at.</p>
      <p class="glossary__item glossary__item--pink"><span class="glossary__term">3D</span> is an image of the fetus and its features - So you can see the baby has dad’s nose, and mom’s lips.</p>
      <p class="glossary__item glossary__item--blue"><span class="glossary__term">4D</span> is 3D, but with motion - You can see baby yawn, move its arm, or even give you a smile.</p>
      <p class="glossary__item glossary__item--pink"><span class="glossary__term">HD</span> is also 3D, but better - Now, you can see a rendering of baby’s skin, making it the most realistic fetal image possible … we are one of the few in Los Angeles that have the newest HD-capable machines.</p>
    </div>
    <div class="photo glossary__photo" role="img" aria-label="Photo of hands holding an ultrasound print against a pregnant belly"></div>
  </article>
</section>

</body>
</html>
```